It's a new electrical company based in Newcastle NSW. I would like a logo between the two words "BRANO (insert logo) VOLT". I would like the logo to represent electrical and celtic style. For example I have seen a light bulb with a celtic pattern in the middle which looked very good. I would like it to be a white card, mainly black writing and quite basic not too much going on. But maybe have the logo partially red or green?

Reason: Waiting for new e mail address so I can put it on the business card

Industry/Entity Type

Electrical

Contact Information for Business Card

BRANO VOLT
Electrical Contractors
Domestic, commercial, fault finding, testing, re wires, switchboard upgrades
License No: 730482K
Fully Insured
Phone: 0487310294

```html
<!DOCTYPE html>
<html lang="en">
<head>
<meta charset="utf-8">
<title>BRANO VOLT – Business Card</title>
<link rel="stylesheet" href="https://fonts.googleapis.com/css2?family=Open+Sans:wght@700&family=Roboto:wght@300;400;700&display=swap">
<style>
  :root {
    --page-bg: #e6e6e6;
    --card-white: #ffffff;
    --ink-dark: #2b2b2d;
    --band-dark: #2c2c2e;
    --accent-red: #e21f26;
    --text-light: #ffffff;
  }
  html, body {
    margin: 0;
    padding: 0;
    width: 1200px;
    height: 900px;
    overflow: hidden;
    background: var(--page-bg);
  }
  .business-card {
    position: absolute;
    left: 46px;
    top: 131px;
    width: 1107px;
    height: 639px;
    background: var(--card-white);
    overflow: hidden;
  }
  .card-bands {
    position: absolute;
    left: 0;
    top: 0;
    width: 1107px;
    height: 639px;
    display: block;
  }
  .band-dark { fill: var(--band-dark); }
  .band-red { fill: var(--accent-red); }

  .brand-lockup {
    position: absolute;
    left: 42px;
    top: 192px;
    display: flex;
    align-items: center;
    font-family: "Open Sans", Arial, sans-serif;
    font-weight: 700;
    font-size: 78px;
    line-height: 1;
    color: var(--ink-dark);
    white-space: nowrap;
  }
  .brand-dot {
    width: 44px;
    height: 44px;
    margin: 0 20px;
    border-radius: 50%;
    background: var(--accent-red);
  }

  .contact-line {
    position: absolute;
    right: 43px;
    margin: 0;
    font-family: "Roboto", Arial, sans-serif;
    font-weight: 400;
    font-size: 21px;
    line-height: 1;
    color: var(--ink-dark);
    white-space: nowrap;
  }
  .contact-phone { top: 202px; }
  .contact-license { top: 244px; }

  .footer-dot {
    position: absolute;
    left: 60px;
    top: 535px;
    width: 18px;
    height: 18px;
    border-radius: 50%;
    background: var(--text-light);
  }
  .footer-line {
    position: absolute;
    left: 124px;
    margin: 0;
    font-family: "Roboto", Arial, sans-serif;
    font-weight: 300;
    font-size: 24px;
    line-height: 1;
    color: var(--text-light);
    white-space: nowrap;
  }
  .footer-intro { top: 530px; }
  .footer-services { top: 560px; }
  .footer-brand { font-weight: 700; }
  .service-highlight { color: var(--accent-red); }
</style>
</head>
<body>
  <div class="business-card" aria-label="BRANO VOLT business card">
    <svg class="card-bands" viewBox="0 0 738 426" aria-hidden="true">
      <polygon class="band-red" points="296,322 417,276 521,303 738,264 738,316 516,335"/>
      <polygon class="band-dark" points="0,311 197,285 296,322 417,285 516,335 738,316 738,416 0,416"/>
      <rect class="band-red" x="0" y="416" width="738" height="10"/>
    </svg>

    <div class="brand-lockup">
      <span class="brand-word">BRANO</span>
      <span class="brand-dot" aria-hidden="true"></span>
      <span class="brand-word">VOLT</span>
    </div>

    <p class="contact-line contact-phone">Phone: 048 73 10 294</p>
    <p class="contact-line contact-license">License No: 730482K Fully Insured</p>

    <span class="footer-dot" aria-hidden="true"></span>
    <p class="footer-line footer-intro"><span class="footer-brand">BRANO VOLT</span> Electrical Contractors Domestic</p>
    <p class="footer-line footer-services"><span class="service-highlight">commercial</span> - fault finding - <span class="service-highlight">testing</span> - re wires - <span class="service-highlight">switchboard upgrades</span></p>
  </div>
</body>
</html>
```